Wine label - premium, elegant & classic

We are a young husband and wife team who have worked in the wine industry for 10+ years. This year we've finally had the opportunity to make our own wine and release our own brand. Our wines are boutique and sell at a mid-premium price (we don't make a lot) so we're looking for a label design that can reflect this premium nature and mixes traditional design elements with modern reflections.

The brand is called: L&T

Reason: We've received some great design concepts over the past week which we would happily pay for, so we've decided to guarantee payment and extend the deadline to allow time for more designs to be sent through. A BIG thanks to all who have already submitted, your designs are still under consideration. Cheers, T.

A big thank you to all for taking the time to submit your beautiful designs to our project.  We now have the very tough job of looking over each of them and selecting only one.  We hope to come to a decision in the next day or two, so hopefully we won't keep you waiting too long!

Cheers, and thanks again

L&T.                                   

Target Market(s)

30 - 45 year old female and male wine drinkers

Requirements
Must have
• Can we please see two versions of the one design - one for a red wine and one for a white wine.

The front labels needs to include the following information:
1. Brand name: L&T
2. Wine varieties: Pinot Noir (red wine) and Sauvignon Blanc (white wine)
3. Vintage: 2012 for both
4. Region: Yarra Valley
5. GI: Wine of Australia (not essential to be on front label)

The back label needs to include the following:
1. The brand name: L&T
2. Variety, vintage, region and volume (the volume must be 4mm in height)
3. Room for product description - approx. 30-40 words.
4. Alcohol statement (no size restriction, pls use 12.5% ALC/VOL as example)
5. Standard drinks (no size restriction, pls use 'Approx.7.8 standard drinks' as example)
6. Sulphites statement: "Sulphites added."
7. Allergen statement: "Fined with the aid of egg and milk products and traces may remain."
8. Room for address: Approx. 20 words
9. "Wine of Australia" - no size restriction, just needs to be legible

Packaging presentation:
Pinot Noir is a red wine and Sauvignon Blanc is a white wine.
Labels for both need to be shown on premium punted burgundy bottles (pls see example: http://www.velmorapack.com/products_services/kfq_premium_burgundy_750_ml_wine_bottle.html)
Nice to have
• We would like the design to embody the following elements:
1. Classically modern
2. Clean and simple
3. Elegance
4. Restricted use of colours (ideally just black/grey, white/buff and perhaps one other)

Some design examples of what we like:
1. http://www.fernandgulls.com.au/sangiovese-tasting-notes/
2. http://quollridge.com/Wines/Quoll-Ridge-Vineyard/Range/2010-Quoll-Ridge-Single-Vineyard-Pinot-Noir-.htm
Should not have
• Preferrably won't have any photos or drawings unless you feel there is a simple symbol or image that could be used to enhance the design.

Restricted use of colours - more muted, conservative tones.

```html
<!DOCTYPE html>
<html lang="en">
<head>
<meta charset="utf-8">
<title>L&amp;T — Wine Label Presentation</title>
<link href="https://fonts.googleapis.com/css2?family=Cormorant+Garamond:wght@500;600;700&display=swap" rel="stylesheet">
<style>
  :root {
    --ink: #000000;
    --paper: #ffffff;
    --rule: #333333;
    --glass-light: #4a4c34;
    --glass-mid: #24261a;
    --glass-dark: #0d0e09;
    --serif: "Cormorant Garamond", "Times New Roman", serif;
  }
  * { box-sizing: border-box; margin: 0; padding: 0; }
  html, body { width: 1200px; height: 900px; overflow: hidden; background: var(--paper); }
  .sheet { position: relative; width: 1200px; height: 900px; font-family: var(--serif); color: var(--ink); }

  .brand-block { position: absolute; left: 0; top: 0; width: 290px; height: 290px; background: var(--ink); color: var(--paper); }
  .brand-block .mark { position: absolute; left: 34px; top: 96px; font-size: 124px; font-weight: 500; line-height: 1; letter-spacing: -2px; }
  .mark .amp { font-size: 0.48em; letter-spacing: 0; }

  /* bottles */
  .bottle { position: absolute; top: 35px; width: 114px; height: 383px; border-radius: 40px 40px 10px 10px;
    background: linear-gradient(90deg, var(--glass-dark) 0%, var(--glass-light) 30%, var(--glass-mid) 60%, var(--glass-dark) 100%); }
  .bottle-1 { left: 424px; } .bottle-2 { left: 577px; } .bottle-3 { left: 836px; } .bottle-4 { left: 986px; }

  /* mini front label */
  .mini-front { position: absolute; left: 0; top: 228px; width: 114px; height: 124px; font-variant: small-caps; text-align: center; }
  .mini-front .band { position: absolute; left: 0; top: 0; width: 114px; height: 46px; }
  .mini-front .cap { position: absolute; left: 30px; top: 0; width: 53px; height: 46px; font-size: 17px; font-weight: 500; line-height: 46px; }
  .mini-front .var { position: absolute; left: 30px; top: 46px; width: 53px; height: 39px; font-size: 6px; font-weight: 600; line-height: 1.05; padding-top: 8px; }
  .mini-front .var .yr { font-size: 5px; font-weight: 500; margin-top: 6px; }
  .mini-front .base { position: absolute; left: 30px; top: 85px; width: 53px; height: 39px; font-size: 4.5px; line-height: 1.15; padding-top: 25px; }
  .front-white .band, .front-white .var { background: var(--paper); color: var(--ink); }
  .front-white .cap, .front-white .base { background: var(--ink); color: var(--paper); }
  .front-red .band, .front-red .var { background: var(--ink); color: var(--paper); }
  .front-red .cap, .front-red .base { background: var(--paper); color: var(--ink); }

  /* mini back label */
  .mini-back { position: absolute; left: 0; top: 228px; width: 114px; font-variant: small-caps; }
  .mini-back .head { position: relative; height: 42px; padding: 3px 5px; font-size: 4.5px; line-height: 1.1; }
  .mini-back .head .nm { font-size: 8px; font-weight: 700; }
  .mini-back .head .vol { position: absolute; right: 5px; top: 24px; text-align: right; font-size: 6px; font-weight: 700; font-variant: normal; }
  .mini-back .body { position: relative; height: 78px; padding: 4px 5px; font-size: 3.8px; line-height: 1.2; }
  .mini-back .body .st { margin-top: 4px; }
  .mini-back .body .og { position: absolute; right: 6px; top: 44px; }
  .mini-back .body .ad { position: absolute; left: 5px; bottom: 4px; }
  .back-white .head, .back-red .body { background: var(--ink); color: var(--paper); }
  .back-white .body, .back-red .head { background: var(--paper); color: var(--ink); }

  .variety-caption { position: absolute; top: 430px; width: 300px; text-align: center; font-size: 24px; font-weight: 700; font-variant: small-caps; letter-spacing: 0.5px; }
  .caption-white { left: 407px; } .caption-red { left: 818px; }

  /* flat label layout */
  .label-strip { position: absolute; left: 27px; top: 495px; width: 858px; height: 128px; border: 1px solid var(--rule); }
  .front-cap { position: absolute; left: 392px; top: 495px; width: 127px; height: 128px; background: var(--ink); color: var(--paper); }
  .front-cap .mark { position: absolute; left: 0; right: 0; top: 42px; text-align: center; font-size: 44px; font-weight: 500; line-height: 1; }
  .front-variety { position: absolute; left: 392px; top: 622px; width: 127px; height: 127px; border: 1px solid var(--rule); text-align: center; font-variant: small-caps; }
  .front-variety .name { margin-top: 28px; font-size: 19px; font-weight: 600; line-height: 1; }
  .front-variety .vintage { margin-top: 22px; font-size: 15px; }
  .front-base { position: absolute; left: 392px; top: 748px; width: 127px; height: 127px; background: var(--ink); color: var(--paper); text-align: center; font-variant: small-caps; font-size: 12px; line-height: 1.15; padding-top: 89px; }

  .back-head { position: absolute; left: 885px; top: 495px; width: 287px; height: 128px; background: var(--ink); color: var(--paper); padding: 10px 13px; font-variant: small-caps; }
  .back-head .mark { font-size: 20px; font-weight: 700; line-height: 1.1; }
  .back-head .detail { font-size: 14px; line-height: 1.05; }
  .back-head .volume { position: absolute; right: 14px; top: 84px; text-align: right; font-size: 17px; font-weight: 700; line-height: 1.05; font-variant: normal; }
  .back-body { position: absolute; left: 885px; top: 622px; width: 287px; height: 254px; border: 1px solid var(--rule); padding: 10px 12px; font-variant: small-caps; font-size: 10.6px; line-height: 1.27; }
  .back-body .description { text-align: justify; letter-spacing: -0.1px; }
  .back-body .statements { margin-top: 12px; }
  .back-body .origin { position: absolute; right: 28px; top: 145px; font-size: 11px; font-weight: 600; }
  .back-body .address { position: absolute; left: 12px; top: 184px; line-height: 1.2; }
</style>
</head>
<body>
<main class="sheet">
  <div class="brand-block"><span class="mark">L<span class="amp">&amp;</span>T</span></div>

  <div class="bottle bottle-1" role="img" aria-label="Burgundy bottle with Sauvignon Blanc front label">
    <div class="mini-front front-white">
      <div class="band"></div>
      <div class="cap">L<span class="amp">&amp;</span>T</div>
      <div class="var"><p>Sauvignon<br>Blanc</p><p class="yr">2012</p></div>
      <div class="base"><p>Yarra Valley</p><p>Wine of Australia</p></div>
    </div>
  </div>
  <div class="bottle bottle-2" role="img" aria-label="Burgundy bottle with Sauvignon Blanc back label">
    <div class="mini-back back-white">
      <div class="head"><p class="nm">L&amp;T</p><p>Sauvignon Blanc</p><p>2012</p><p>Yarra Valley</p><p class="vol">750 ml<br>12.5% Alc/vol</p></div>
      <div class="body">
        <p>Crisp and lively with notes of citrus, passionfruit and fresh cut grass over a clean mineral finish.</p>
        <p class="st">Approx.7.8 standard drinks<br>Sulphites added<br>Fined with egg and milk products</p>
        <p class="og">Wine of Australia</p>
        <p class="ad">Street Address<br>14 Larch Lane<br>Fernbrook<br>NSW, 2011</p>
      </div>
    </div>
  </div>
  <div class="bottle bottle-3" role="img" aria-label="Burgundy bottle with Pinot Noir front label">
    <div class="mini-front front-red">
      <div class="band"></div>
      <div class="cap">L<span class="amp">&amp;</span>T</div>
      <div class="var"><p>Pinot<br>Noir</p><p class="yr">2012</p></div>
      <div class="base"><p>Yarra Valley</p><p>Wine of Australia</p></div>
    </div>
  </div>
  <div class="bottle bottle-4" role="img" aria-label="Burgundy bottle with Pinot Noir back label">
    <div class="mini-back back-red">
      <div class="head"><p class="nm">L&amp;T</p><p>Pinot Noir</p><p>2012</p><p>Yarra Valley</p><p class="vol">750 ml<br>12.5% Alc/vol</p></div>
      <div class="body">
        <p>Silky and fragrant with red cherry, forest floor and gentle spice over fine, soft tannins.</p>
        <p class="st">Approx.7.8 standard drinks<br>Sulphites added<br>Fined with egg and milk products</p>
        <p class="og">Wine of Australia</p>
        <p class="ad">Street Address<br>14 Larch Lane<br>Fernbrook<br>NSW, 2011</p>
      </div>
    </div>
  </div>
  <p class="variety-caption caption-white">Sauvignon Blanc</p>
  <p class="variety-caption caption-red">Pinot Nioir</p>

  <div class="label-strip"></div>
  <div class="front-cap"><span class="mark">L<span class="amp">&amp;</span>T</span></div>
  <div class="front-variety">
    <p class="name">Sauvignon<br>Blanc</p>
    <p class="vintage">2012</p>
  </div>
  <div class="front-base"><p>Yarra Valley</p><p>Wine of Australia</p></div>

  <div class="back-head">
    <p class="mark">L&amp;T</p>
    <p class="detail">Sauvignon Blanc</p>
    <p class="detail">2012</p>
    <p class="detail">Yarra Valley</p>
    <p class="volume">750 ml<br>12.5%&nbsp; Alc/vol</p>
  </div>
  <div class="back-body">
    <p class="description">Omni ipic tem quam sitibus dolora sapitate doluptati as maion plaboreptas et quis eum quid endist autatur am iur seres ma intem qui berferae volupta aperspello tem re nullit dis plaboreptas et quis eum.</p>
    <p class="statements">Approx.7.8 standard drinks<br>Sulphites added<br>Fined with the aid of egg and milk products<br>and traces may remain.</p>
    <p class="origin">Wine of Australia</p>
    <p class="address">Street Address<br>14 Larch Lane<br>Fernbrook<br>NSW, 2011<br>Australia</p>
  </div>
</main>
</body>
</html>
```